Update Business Card Design

I'm looking to update my business cards. Attached is a photo of the current design. I like the black side so that does not have to be update. The white side needs to be updated. I want the design to be modern and minimalistic.
I am a lawyer and my firm's website is www.brennoxlegalco.com (for reference).
My firm's logo has a horizontal version (which is on the black side of the card) and a vertical version (on the white side). I would prefer to keep the vertical version on the white side and horizontal version on the black side (the logo files are attached).

I am open to redesigning the black side also. I would like one side to have the horizontal logo and the other to have the vertical logo.

```html
<!DOCTYPE html>
<html lang="en">
<head>
<meta charset="utf-8">
<title>Brennox Legal Co. — Business Card</title>
<link rel="stylesheet" href="https://fonts.googleapis.com/css2?family=Tinos:wght@400;700&display=swap">
<style>
  :root {
    --page: #e9e6e1;
    --teal-deep: #0a5a6e;
    --teal-mid: #1390ae;
    --teal-light: #22b6d6;
    --ink: #050708;
    --ink-soft: #0d262d;
    --cyan: #1fb4dc;
    --paper: #f2f2f2;
  }
  * { box-sizing: border-box; margin: 0; padding: 0; }
  html, body { width: 1200px; height: 900px; overflow: hidden; }
  body {
    background: var(--page);
    font-family: "Tinos", "Times New Roman", serif;
    position: relative;
  }
  .card {
    position: absolute;
    width: 680px;
    height: 388px;
    border-radius: 34px;
    overflow: hidden;
    box-shadow: 0 10px 26px rgba(0,0,0,.22);
  }

  /* Front side */
  .card--front {
    left: 150px; top: 40px;
    background: linear-gradient(100deg, var(--teal-deep) 0%, var(--teal-mid) 30%, var(--teal-light) 52%, var(--teal-mid) 74%, var(--teal-deep) 100%);
  }
  .front-surface {
    position: absolute; inset: 0;
    background:
      radial-gradient(ellipse at 52% 50%, rgba(255,255,255,.10) 0%, rgba(255,255,255,0) 55%),
      linear-gradient(180deg, rgba(0,0,0,0) 60%, rgba(0,0,0,.10) 100%);
  }
  .front-mark {
    position: absolute;
    right: 48px; top: 150px;
    display: flex; align-items: center; gap: 12px;
  }
  .front-mark__dot {
    width: 30px; height: 30px; border-radius: 50%;
    background: #ffffff;
  }
  .front-mark__name {
    color: #ffffff;
    font-size: 24px;
    font-weight: 700;
    letter-spacing: .03em;
  }

  /* Back side */
  .card--back {
    left: 370px; top: 472px;
    background: var(--ink);
    color: var(--paper);
  }
  .back-glow {
    position: absolute; left: 30px; bottom: -40px;
    width: 420px; height: 330px;
    background: radial-gradient(ellipse at 45% 60%, var(--ink-soft) 0%, rgba(13,38,45,.6) 40%, rgba(13,38,45,0) 72%);
  }
  .person {
    position: absolute; left: 34px; top: 146px;
  }
  .person__name {
    color: var(--cyan);
    font-weight: 700;
    font-size: 22px;
    letter-spacing: .02em;
    text-transform: uppercase;
  }
  .person__title { font-size: 17px; margin-top: 4px; }
  .person__mobile { font-size: 17px; margin-top: 6px; display: flex; align-items: center; gap: 10px; }
  .contact {
    position: absolute; left: 340px; top: 62px;
    list-style: none;
    font-size: 16px;
  }
  .contact li { display: flex; align-items: flex-start; gap: 9px; line-height: 23px; }
  .contact .icon { width: 15px; height: 15px; margin-top: 4px; flex: none; }
  .contact .accent { color: var(--cyan); }
  .divider {
    position: absolute; left: 340px; right: 40px; top: 244px;
    height: 1px; background: var(--cyan); opacity: .7;
  }
  .lockup {
    position: absolute; right: 44px; top: 262px;
    display: flex; align-items: center; gap: 16px;
  }
  .lockup__dot { width: 46px; height: 46px; border-radius: 50%; background: var(--cyan); }
  .lockup__name {
    color: var(--cyan);
    font-size: 34px;
    line-height: 1.02;
    letter-spacing: .03em;
    text-transform: uppercase;
  }
</style>
</head>
<body>

<section class="card card--front">
  <div class="front-surface" role="img" aria-label="Repeating embossed firm monogram pattern across the teal surface"></div>
  <div class="front-mark">
    <div class="front-mark__dot"></div>
    <div class="front-mark__name">Brennox Legal Co.</div>
  </div>
</section>

<section class="card card--back">
  <div class="back-glow" role="img" aria-label="Large faint firm monogram in dark teal"></div>

  <div class="person">
    <div class="person__name">Daniel Merrow</div>
    <div class="person__title">Founder | Attorney of Brennox Legal Co.</div>
    <div class="person__mobile">
      <svg width="12" height="18" viewBox="0 0 12 18" fill="none" stroke="#1fb4dc" stroke-width="1.4"><rect x="1" y="1" width="10" height="16" rx="2"/><line x1="5" y1="14" x2="7" y2="14"/></svg>
      310.555.0163
    </div>
  </div>

  <ul class="contact">
    <li><svg class="icon" viewBox="0 0 16 16" fill="#1fb4dc"><path d="M3 1l3 3-1.5 2a9 9 0 005.5 5.5L12 10l3 3-2 2C7 15 1 9 1 3z"/></svg>877.555.0142</li>
    <li><svg class="icon" viewBox="0 0 16 16" fill="#1fb4dc"><rect x="4" y="1" width="8" height="4"/><rect x="1" y="6" width="14" height="6" rx="1"/><rect x="4" y="10" width="8" height="5" fill="#050708" stroke="#1fb4dc"/></svg>310.555.0187</li>
    <li><svg class="icon" viewBox="0 0 16 16" fill="none" stroke="#1fb4dc" stroke-width="1.5"><rect x="1" y="3" width="14" height="10"/><path d="M1 3l7 6 7-6"/></svg><span>daniel@<span class="accent">BrennoxLegalCo</span>.com</span></li>
    <li><svg class="icon" viewBox="0 0 16 16" fill="none" stroke="#1fb4dc" stroke-width="1.2"><circle cx="8" cy="8" r="7"/><ellipse cx="8" cy="8" rx="3" ry="7"/><line x1="1" y1="8" x2="15" y2="8"/></svg><span>www.<span class="accent">brennoxlegalco</span>.com</span></li>
    <li><svg class="icon" viewBox="0 0 16 16" fill="#1fb4dc"><path d="M8 1a5 5 0 015 5c0 4-5 9-5 9S3 10 3 6a5 5 0 015-5z"/><circle cx="8" cy="6" r="2" fill="#050708"/></svg><span>1180 Larkmont Avenue, Suite 310<br>Westbrook, CA 90412</span></li>
  </ul>

  <div class="divider"></div>

  <div class="lockup">
    <div class="lockup__dot"></div>
    <div class="lockup__name">Brennox<br>Legal Co.</div>
  </div>
</section>

</body>
</html>
```